Wine Label named: Amber Ridge

We are a wine producer, who wishes to launch a new premium wine called: Amber Ridge
Our winery is situated in a rolling hill, with slopes, where Amber Ridge exists in the property. One dates to the 15th century and the other more recent to the 18th century. Its a unique feature of the winery and we wish to create a label that represents these, but is NOT religious! Difficult task I know. Think you can pull it off? Let us see it! We start with one label, but the winner will have 5 more labels to design.

Target Market(s)

30-50 year old men

Industry/Entity Type

Wine

Colors

Designer to choose colors to be used in the design.

Requirements
Must have
• serious look and premium feel. name of the wine: Amber Ridge
Nice to have
• 2019 14% ABV
Should not have
• a religious look and feel

```html
<!DOCTYPE html>
<html lang="en">
<head>
<meta charset="utf-8">
<title>Amber Ridge – Wine Label</title>
<link rel="stylesheet" href="https://fonts.googleapis.com/css2?family=Cormorant+Garamond:wght@500;600&family=Montserrat:wght@400&display=swap">
<style>
  :root {
    --backdrop: #c8bba6;
    --label-light: #e4e4d2;
    --label-mid: #d3d4b8;
    --label-deep: #c0c19f;
    --ink: #6b6b50;
    --rule: #f6f6ee;
    --scene-deep: #74765a;
    --scene-soft: #9c9d7e;
  }
  * { margin: 0; padding: 0; box-sizing: border-box; }
  html, body {
    width: 1200px;
    height: 923px;
    overflow: hidden;
    background: var(--backdrop);
  }
  .label {
    position: absolute;
    left: 345px;
    top: 37px;
    width: 510px;
    height: 848px;
    overflow: hidden;
    background:
      linear-gradient(115deg, rgba(255,255,255,0) 30%, rgba(255,255,255,0.35) 48%, rgba(255,255,255,0) 66%),
      linear-gradient(180deg, var(--label-deep) 0%, var(--label-mid) 30%, var(--label-light) 58%, var(--label-mid) 100%);
    color: var(--ink);
    text-align: center;
  }
  .label__frame {
    position: absolute;
    border: 1.5px solid var(--rule);
    z-index: 2;
  }
  .label__frame--outer { inset: 14px 11px 10px 11px; }
  .label__frame--inner { inset: 24px 21px 20px 21px; }
  .label__name {
    position: absolute;
    left: 0;
    right: 0;
    top: 140px;
    font-family: "Cormorant Garamond", "Times New Roman", serif;
    font-weight: 600;
    font-size: 84px;
    line-height: 64px;
    letter-spacing: -0.5px;
  }
  .label__vintage {
    position: absolute;
    left: 0;
    right: 0;
    top: 368px;
    font-family: "Cormorant Garamond", "Times New Roman", serif;
    font-weight: 500;
    font-size: 36px;
    line-height: 40px;
    font-variant-numeric: lining-nums;
    letter-spacing: 1px;
  }
  .label__divider {
    position: absolute;
    left: 49px;
    right: 51px;
    top: 418px;
    height: 1.5px;
    background: var(--rule);
  }
  .label__style {
    position: absolute;
    left: 0;
    right: 0;
    top: 423px;
    font-family: "Montserrat", Arial, sans-serif;
    font-size: 14px;
    letter-spacing: 3.2px;
    line-height: 18px;
  }
  .label__abv {
    position: absolute;
    left: 0;
    right: 0;
    top: 446px;
    font-family: "Montserrat", Arial, sans-serif;
    font-size: 14px;
    letter-spacing: 0.5px;
    line-height: 18px;
  }
  .label__scene {
    position: absolute;
    left: 0;
    top: 470px;
    width: 510px;
    height: 378px;
    display: block;
  }
</style>
</head>
<body>
  <main class="label">
    <svg class="label__scene" viewBox="0 0 510 378" role="img" aria-label="Sketched illustration of two old stone buildings on a rolling hill above rows of vines">
      <defs>
        <linearGradient id="scene-fill" x1="0" y1="0" x2="0" y2="1">
          <stop offset="0" stop-color="var(--scene-soft)" stop-opacity="0.55"/>
          <stop offset="0.45" stop-color="var(--scene-deep)" stop-opacity="0.85"/>
          <stop offset="1" stop-color="var(--scene-deep)" stop-opacity="0.9"/>
        </linearGradient>
      </defs>
      <path fill="url(#scene-fill)" d="M0 238 C55 228 88 214 96 160 C104 110 190 70 270 40 C330 72 378 118 396 200 C432 214 478 214 510 210 L510 362 L0 362 Z"/>
    </svg>
    <div class="label__frame label__frame--outer"></div>
    <div class="label__frame label__frame--inner"></div>
    <h1 class="label__name">amber<br>ridge</h1>
    <p class="label__vintage">2019</p>
    <div class="label__divider"></div>
    <p class="label__style">PREMIUM RED WINE</p>
    <p class="label__abv">14% ABV</p>
  </main>
</body>
</html>
```